2 sets of Business cards, stationary/envelopes, stationary template(MS Word), door hang tag
KRV Building Works, LLC (Design A) and Steadfield Estate Holdings, LLC (Design B)
2 sets of Business cards, stationary/envelopes, stationary template(MS Word), door hang tag - Real Estate
Creative Brief
Simple
Darrel K. Winton
Managing Member
5120 Larkspur Lane, Suite B Columbia, MO 65201
Don't know yet, but need space for it
dwinton@krvbuildworks.com
www.krvbuildworks.com (Design A) and www.steadfieldleasing.com (Design B)
We are a family owned business with 90+ years in the construction and real estate sector and would like to present our company as a quality, professional organization with a sleek modern set of stationary. Stationary design A: Company name: KRV Building Works, LLC Optional Tagline: Working from experience, not for it! Color Mode: RGB color Grey :R=149 G=149 B=149 White: R=255 G=255 B=255 Black : R=0 G=0 B=0 Blue : R=0 G=97 B=240 dwinton@krvbuildworks.com (Design A) For: KRV Building Works, LLC Stationary design B: Company name: Steadfield Estate Holdings, LLC Optional Tagline: Steadfield Precision, Steadfield Dedication Color Mode: RGB color Grey :R=149 G=149 B=149 White: R=255 G=255 B=255 Black : R=0 G=0 B=0 Red : R=209 G=0 B=0 dwinton@steadfieldleasing.com (Design B) For: Steadfield Estate Holdings, LLC Phone, email, and name will change for the additional members of the company. We also want an electronic email signature, and digital stationary template (MS word). Stationary and envelopes should tie in the theme of the business cards for a uniform look. Also looking for a Header only version of the stationary, as well as a full page version (header and footer used for design).
Logo used in a creative way.
darrelkwinton darrelkwinton
Sorry, been out of the office. Waiting for partners to look at everything before making comments. We should be leaving comments and making recommendations in the next day or two for all of the designs we want to see refined. Thanks, Darrel

```html
<!DOCTYPE html>
<html lang="en">
<head>
<meta charset="utf-8">
<title>KRV Building Works – Business Card</title>
<link href="https://fonts.googleapis.com/css2?family=Open+Sans:wght@400;600&display=swap" rel="stylesheet">
<style>
  :root {
    --page: #e9e7e3;
    --card: #ffffff;
    --ink: #000000;
    --grey: #959595;
    --blue: #0061f0;
    --paper-text: #ffffff;
  }
  html, body {
    margin: 0;
    padding: 0;
    width: 1200px;
    height: 1086px;
    overflow: hidden;
    background: var(--page);
    font-family: "Open Sans", Arial, sans-serif;
  }
  .card {
    position: absolute;
    left: 250px;
    width: 700px;
    height: 400px;
    background: var(--card);
    box-shadow: 0 2px 10px rgba(0,0,0,0.12);
    overflow: hidden;
  }
  .card--front { top: 95px; }
  .card--back { top: 591px; }

  .brand {
    position: absolute;
    left: 250px;
    top: 120px;
    display: flex;
    align-items: center;
    gap: 14px;
  }
  .brand__square {
    width: 34px;
    height: 34px;
    background: var(--blue);
  }
  .brand__name {
    font-size: 30px;
    font-weight: 600;
    color: var(--grey);
    letter-spacing: 1px;
  }
  .brand__rule {
    position: absolute;
    left: 250px;
    top: 178px;
    width: 260px;
    height: 3px;
    background: var(--blue);
  }
  .person {
    position: absolute;
    right: 150px;
    top: 222px;
    text-align: right;
    color: var(--ink);
  }
  .person__name {
    font-size: 22px;
    letter-spacing: 2px;
    font-weight: 400;
    margin: 0;
  }
  .person__title {
    font-size: 16px;
    margin: 6px 0 0;
    color: #333;
  }

  .card__art {
    position: absolute;
    left: 0;
    top: 0;
  }
  .contact {
    position: absolute;
    right: 345px;
    color: var(--paper-text);
    font-size: 15px;
    line-height: 1.45;
    text-align: right;
  }
  .contact--phone { top: 70px; }
  .contact--address { top: 176px; }
  .contact--web { top: 281px; }
</style>
</head>
<body>
  <section class="card card--front">
    <div class="brand">
      <span class="brand__square"></span>
      <span class="brand__name">KRV Building Works</span>
    </div>
    <div class="brand__rule"></div>
    <div class="person">
      <p class="person__name">DARREL WINTON</p>
      <p class="person__title">Managing Director</p>
    </div>
  </section>

  <section class="card card--back">
    <svg class="card__art" width="700" height="400" viewBox="0 0 700 400">
      <rect x="0" y="0" width="400" height="400" fill="var(--ink)"/>
      <circle cx="400" cy="95" r="40" fill="var(--ink)"/>
      <circle cx="400" cy="200" r="40" fill="var(--ink)"/>
      <circle cx="400" cy="305" r="40" fill="var(--ink)"/>
      <g fill="none" stroke="var(--paper-text)" stroke-width="2">
        <circle cx="405" cy="95" r="18"/>
        <circle cx="405" cy="200" r="18"/>
        <circle cx="405" cy="305" r="18"/>
      </g>
      <!-- phone -->
      <path d="M398 86 q-3 3 0 9 q4 8 11 11 q5 2 7-1 l-4-4 q-2 2-4 0 q-4-3-6-7 q-1-2 1-3 z" fill="var(--paper-text)"/>
      <!-- pin -->
      <path d="M405 210 q-9-10-9-15 a9 9 0 0 1 18 0 q0 5-9 15 z" fill="var(--paper-text)"/>
      <circle cx="405" cy="195" r="3" fill="var(--ink)"/>
      <!-- globe -->
      <g fill="none" stroke="var(--paper-text)" stroke-width="1.6">
        <circle cx="405" cy="305" r="10"/>
        <ellipse cx="405" cy="305" rx="4.5" ry="10"/>
        <line x1="395" y1="305" x2="415" y2="305"/>
      </g>
    </svg>
    <div class="contact contact--phone">555 014 2236<br>555 014 2237</div>
    <div class="contact contact--address">5120 Larkspur Lane, Suite B<br>Columbia, MO 65201</div>
    <div class="contact contact--web">dwinton@krvbuildworks.com<br>www.krvbuildworks.com</div>
  </section>
</body>
</html>
```